Meridane Works, Inc. - Update our Website

Meridane Works needs a website to help our customers to navigate through our services efficiently. Our existing website is at www.meridwork.example

We would like to explain our services with content and pictures (photographs) that distinguishes our products and services from our competition.

The website design must implement a strategy to focus on our Contract Labeling services.

With this new design we would like to attract new customers and ensure that our existing customers are fully informed with our latest offerings.

```html
<!DOCTYPE html>
<html lang="en">
<head>
<meta charset="utf-8">
<title>Meridane Works, Inc.</title>
<link href="https://fonts.googleapis.com/css2?family=Roboto:wght@400;500;700&family=Roboto+Condensed:wght@700&family=Michroma&display=swap" rel="stylesheet">
<style>
:root{
  --blue:#0b6faa;
  --orange:#f97a0e;
  --green:#7cc21a;
  --ink:#1d1d1d;
  --white:#ffffff;
  --divider:#2f86bb;
}
*{margin:0;padding:0;box-sizing:border-box}
html,body{width:1200px;height:758px;overflow:hidden;background:var(--white);font-family:'Roboto',sans-serif}
.page{position:relative;width:1200px;height:758px}
.masthead{position:absolute;left:0;top:0;width:1200px;height:110px;background:var(--white)}
.brand{position:absolute;left:174px;top:34px;display:flex;align-items:center;gap:12px}
.brand-dot{width:40px;height:40px;border-radius:50%;background:var(--green)}
.brand-name{font-family:'Roboto',sans-serif;font-weight:700;font-size:28px;color:var(--ink);letter-spacing:1px;text-transform:uppercase}
.phone{position:absolute;right:172px;top:38px;display:flex;align-items:center;gap:10px;color:var(--blue);font-size:18px}
.mainnav{position:absolute;left:0;top:110px;width:1200px;height:40px;background:var(--blue)}
.mainnav ul{list-style:none;position:absolute;left:171px;top:0;display:flex;height:40px}
.mainnav li{height:40px;line-height:40px;text-align:center;color:var(--white);font-size:14px;border-right:1px solid var(--divider)}
.mainnav li:last-child{border-right:none}
.mainnav li.active{background:var(--orange)}
.hero{position:absolute;left:0;top:150px;width:1200px;height:429px;overflow:hidden}
.hero-photo{position:absolute;inset:0;background:linear-gradient(90deg,#e9ecef 0%,#dfe3e8 30%,#b9c3d1 60%,#9aa8bd 100%)}
.hero-copy{position:absolute;right:199px;top:104px;text-align:right}
.hero-kicker{font-family:'Roboto Condensed',sans-serif;font-weight:700;font-size:21px;color:var(--white)}
.hero-focus{font-family:'Roboto Condensed',sans-serif;font-weight:700;font-size:66px;line-height:60px;color:var(--green);-webkit-text-stroke:3px var(--ink);paint-order:stroke fill;letter-spacing:2px;margin-top:2px}
.hero-line{font-family:'Roboto Condensed',sans-serif;font-weight:700;font-size:25px;color:#2a2a2a;margin-top:6px}
.hero-subject{font-family:'Michroma',sans-serif;font-size:20px;color:var(--white);letter-spacing:0;margin-top:-2px}
.hero-cta{display:inline-flex;align-items:center;gap:8px;margin-top:14px;height:35px;padding:0 14px 0 16px;background:var(--orange);color:var(--white);font-family:'Roboto Condensed',sans-serif;font-weight:700;font-size:20px;border-radius:2px}
.slide-arrow{position:absolute;top:194px;width:39px;height:39px;border-radius:50%;background:rgba(255,255,255,.55);display:flex;align-items:center;justify-content:center}
.slide-arrow.prev{left:36px}
.slide-arrow.next{right:36px}
.services-tab{position:absolute;left:493px;top:545px;width:214px;height:35px}
.services-tab span{position:absolute;left:0;right:0;top:12px;text-align:center;font-family:'Michroma',sans-serif;font-size:14px;color:var(--ink);font-weight:700}
.services{position:absolute;left:0;top:579px;width:1200px;height:111px;background:var(--white)}
.service{position:absolute;top:22px;width:150px;margin-left:-75px;text-align:center}
.service svg{display:block;margin:0 auto;height:38px}
.service-name{margin-top:18px;color:var(--orange);font-weight:700;font-size:14px}
.footer-rule{position:absolute;left:0;top:688px;width:1200px;height:4px;background:linear-gradient(180deg,#555 0%,#c9c9c9 100%)}
.footer{position:absolute;left:0;top:692px;width:1200px;height:66px;background:var(--blue);color:var(--white)}
.footer-links{position:absolute;left:174px;top:15px;font-size:12px}
.footer-links span.sep{margin:0 5px}
.copyright{position:absolute;left:172px;top:39px;font-size:11px}
.social{position:absolute;right:172px;top:28px;display:flex;gap:19px}
.social span{width:14px;height:14px;border-radius:50%;background:var(--white)}
</style>
</head>
<body>
<div class="page">
  <header class="masthead">
    <div class="brand"><span class="brand-dot"></span><span class="brand-name">Meridane Works, Inc.</span></div>
    <div class="phone">
      <svg width="28" height="28" viewBox="0 0 28 28"><circle cx="14" cy="14" r="13" fill="none" stroke="#333" stroke-width="1.5"/><path d="M10 8c1-1 2-1 2.5 0l1 2c.3.7 0 1.2-.5 1.6l-.7.5c.6 1.6 1.9 2.9 3.5 3.6l.5-.7c.4-.5 1-.8 1.6-.5l2 1c1 .5 1 1.5 0 2.5-1 1-2.5 1.3-4 .6C12.5 17.4 10.5 15.4 9.4 12c-.6-1.5-.4-3 .6-4z" fill="#f97a0e"/></svg>
      <span>+0800 555 0199</span>
    </div>
  </header>

  <nav class="mainnav">
    <ul>
      <li class="active" style="width:106px">Home</li>
      <li style="width:122px">About us</li>
      <li style="width:121px">Services</li>
      <li style="width:121px">Products</li>
      <li style="width:149px">User Support</li>
      <li style="width:101px">Blog</li>
      <li style="width:138px">Contact Us</li>
    </ul>
  </nav>

  <section class="hero">
    <div class="hero-photo" role="img" aria-label="Photograph of a smiling lab professional in a white coat holding a tablet in a bright pharmacy laboratory"></div>
    <div class="hero-copy">
      <div class="hero-kicker">WE ARE FOCUSED ON THE NEEDS OF THOSE</div>
      <div class="hero-focus">INDIVIDUALS</div>
      <div class="hero-line">INVOLVED WITH</div>
      <div class="hero-subject">CLINICAL TRIAL MATERIALS</div>
      <div class="hero-cta">Click here to view more
        <svg width="16" height="16" viewBox="0 0 16 16"><circle cx="8" cy="8" r="8" fill="#fff"/><path d="M5 8h6M8 5l3 3-3 3" stroke="#f97a0e" stroke-width="2" fill="none"/></svg>
      </div>
    </div>
    <div class="slide-arrow prev"><svg width="12" height="20" viewBox="0 0 12 20"><path d="M10 2 2 10l8 8" stroke="#444" stroke-width="1.5" fill="none"/></svg></div>
    <div class="slide-arrow next"><svg width="12" height="20" viewBox="0 0 12 20"><path d="M2 2l8 8-8 8" stroke="#444" stroke-width="1.5" fill="none"/></svg></div>
    <svg class="services-tab" viewBox="0 0 214 35" style="position:absolute;left:493px;top:395px"><path d="M14 0h186l14 35H0z" fill="#fff"/></svg>
  </section>
  <div class="services-tab"><span>OUR SERVICES</span></div>

  <section class="services">
    <div class="service" style="left:236px">
      <svg viewBox="0 0 40 38"><path d="M8 2h28l-6 32H2z" fill="#0b6faa"/><path d="M12 9h18M11 15h18M10 21h18" stroke="#fff" stroke-width="2.5"/><path d="M2 34h28" stroke="#fff" stroke-width="2"/></svg>
      <div class="service-name">MeriBook</div>
    </div>
    <div class="service" style="left:382px">
      <svg viewBox="0 0 42 38"><path d="M6 30C4 16 16 4 40 4 38 24 26 34 12 30z" fill="#0b6faa"/><path d="M2 36C10 26 20 18 32 12" stroke="#fff" stroke-width="2.5" fill="none"/><path d="M2 36 8 30" stroke="#0b6faa" stroke-width="3"/></svg>
      <div class="service-name">MeriServ</div>
    </div>
    <div class="service" style="left:528px">
      <svg viewBox="0 0 40 38"><path d="M2 18C3 8 11 3 20 3s17 5 18 15c-3-3-6-3-9 0-3-3-6-3-9 0-3-3-6-3-9 0-3-3-6-3-9 0z" fill="#0b6faa"/><path d="M20 1v3M20 17v15c0 4-6 4-6 0" stroke="#0b6faa" stroke-width="3" fill="none"/></svg>
      <div class="service-name">Randomizations</div>
    </div>
    <div class="service" style="left:674px">
      <svg viewBox="0 0 30 38"><path d="M0 0h18l12 12v26H0z" fill="#0b6faa"/><path d="M18 0v12h12" fill="#fff" opacity=".5"/><path d="M6 20h18M6 26h18M6 32h18" stroke="#fff" stroke-width="2.5"/></svg>
      <div class="service-name">MeriPro/LBL</div>
    </div>
    <div class="service" style="left:819px">
      <svg viewBox="0 0 42 38"><rect x="2" y="4" width="32" height="32" rx="4" fill="none" stroke="#0b6faa" stroke-width="4"/><path d="M10 18l8 8L40 4" stroke="#0b6faa" stroke-width="5" fill="none"/></svg>
      <div class="service-name">Software Validation</div>
    </div>
    <div class="service" style="left:965px">
      <svg viewBox="0 0 38 34"><path d="M0 3c0-2 1-3 3-3h10l4 5h18c2 0 3 1 3 3v23c0 2-1 3-3 3H3c-2 0-3-1-3-3z" fill="#0b6faa"/></svg>
      <div class="service-name">MeriStock</div>
    </div>
  </section>

  <div class="footer-rule"></div>
  <footer class="footer">
    <div class="footer-links">Home<span class="sep">|</span>About us<span class="sep">|</span>Services<span class="sep">|</span>Products<span class="sep">|</span>User Support<span class="sep">|</span>Blog<span class="sep">|</span>Contact Us</div>
    <div class="copyright">Copyright © 2014</div>
    <div class="social" aria-label="Social links"><span></span><span></span><span></span><span></span></div>
  </footer>
</div>
</body>
</html>
```